Handyman Company needs home page to POP, to grab attention/ image and text. Be 1,000 words...

Looking for a (uncoded) PSD design for Kiosk image and animated text. We are experiencing design block, just cant come up with the right image or font to scream handyman service. This is our template, not looking for structure change. Image or images, colors font ect.... must work within the boxes we have. feel free to graphically design entire home page. Animated message is also up for a change or up grade.
our test site is...http://test.plovernest.com/kql-fixers/
sites that provide like service are: https://www.chorewaffle.com/m/handyman
https://www.bolthelpers.com/
we will require image selected license or source image that can be purchased (pixvault) ect. have fun... If logo is problem we are open to ideas and designs.

The text in kiosk photo can be changed... could just say HANDYMAN.....

Reason: Extension due to new invite as well as submissions are close to deadline. I extended to be sure we get the best design possible. KEEP UP THE GOOD WORK.

Industry/Entity Type

Handyman

Number of Pages Required

1 page

Font styles to use
Serif

Requirements
Must have
• must scream handyman... like chore waffle link above, the image and text don't need explaining. You get to that page and you know what it is...

```html
<!DOCTYPE html>
<html lang="en">
<head>
<meta charset="utf-8">
<title>Quillon Handyman Services</title>
<link rel="stylesheet" href="https://fonts.googleapis.com/css2?family=Oswald:wght@300;400;500;600;700&display=swap">
<style>
:root{
  --navy:#14284f;
  --navy-deep:#102246;
  --ink:#1b1b1b;
  --muted:#6a6a6a;
  --white:#ffffff;
  --accent:#2c9ad8;
  --orange:#f18a1c;
  --red:#e32b2b;
  --green:#6cb030;
  --sky:#2aa9e8;
  --line:#8cc4e0;
  --hero-a:#5a5550;
  --hero-b:#b8b0a4;
}
*{box-sizing:border-box;margin:0;padding:0}
html,body{width:1200px;height:3285px;overflow:hidden}
body{font-family:'Oswald',sans-serif;color:var(--ink);background:var(--white);position:relative}
.abs{position:absolute}

/* header + hero */
.hero{left:0;top:0;width:1200px;height:536px;background:linear-gradient(100deg,var(--hero-a) 0%,#7d746a 35%,#8c857c 60%,var(--hero-b) 100%)}
.hero-shade{left:0;top:0;width:1200px;height:536px;background:rgba(30,30,30,.35)}
.topbar{left:0;top:0;width:1200px;height:92px;background:rgba(255,255,255,.88)}
.brand{left:162px;top:24px;display:flex;align-items:center;gap:10px}
.brand-mark{width:34px;height:34px;background:var(--red)}
.brand-name{font-size:20px;font-weight:600;color:var(--navy);line-height:1.05;width:120px}
.nav{left:510px;top:44px;display:flex;gap:34px;font-size:13px;font-weight:500;color:var(--navy);text-transform:uppercase}
.nav .active{border-bottom:3px solid var(--orange);padding-bottom:6px}
.hero-title{left:0;top:180px;width:1200px;text-align:center;color:var(--white);font-size:86px;font-weight:700;letter-spacing:1px}
.hero-sub{left:0;top:292px;width:1200px;text-align:center;color:var(--white);font-size:36px;font-weight:300}
.hero-cta{left:362px;top:398px;width:476px;height:80px;border:3px solid var(--accent);color:var(--white);font-size:40px;font-weight:400;display:flex;align-items:center;justify-content:center}

/* about */
.h2{font-size:48px;font-weight:600;color:var(--navy);text-transform:uppercase}
.about-title{left:160px;top:560px}
.lead{font-size:13.5px;color:var(--ink)}
.body-sm{font-size:10px;color:var(--muted);line-height:1.4}
.about-lead{left:160px;top:628px;width:880px}
.about-p1{left:160px;top:662px;width:880px;font-size:11px;color:var(--ink)}
.about-p2{left:160px;top:694px;width:880px}

/* why */
.why{left:0;top:785px;width:1200px;height:443px;background:var(--navy)}
.why-title{left:0;top:818px;width:1200px;text-align:center;color:var(--white);font-size:27px;font-weight:400}
.why-intro{left:420px;top:858px;width:360px;text-align:center;color:#dfe5ef;font-size:11px;line-height:1.4}
.why-rule{left:556px;top:902px;width:86px;height:8px;background:var(--white)}
.feature{top:945px;width:230px;text-align:center;color:var(--white)}
.feature svg{display:block;margin:0 auto}
.feature h3{font-size:20px;font-weight:400;margin-top:18px}
.feature p{font-size:10px;color:#c9d2e2;line-height:1.4;margin-top:6px}

/* tips */
.tips-title{left:160px;top:1245px}
.tips-intro{left:160px;top:1305px;width:560px}
.tip{left:160px;width:880px;height:124px}
.tip-photo{position:absolute;left:0;top:0;width:182px;height:124px;background:linear-gradient(135deg,#a9a39b,#6f6a64)}
.tip-body{position:absolute;left:215px;top:0;width:665px}
.tip-body h3{font-size:20px;font-weight:500;color:var(--navy)}
.tip-body p{font-size:9.5px;color:var(--muted);line-height:1.4;margin-top:6px}
.tip-body p b{color:var(--ink)}
.shares{display:flex;gap:8px;margin-top:8px}
.shares span{width:11px;height:11px;border-radius:50%}
.old-posts{left:160px;top:2070px;font-size:20px;font-weight:500;color:var(--navy);display:flex;align-items:center;gap:14px}

/* service area */
.area-panel{left:0;top:2128px;width:375px;height:312px;background:var(--navy)}
.area-title{left:162px;top:2158px;color:var(--white);font-size:24px;font-weight:400}
.area-text{left:162px;top:2198px;width:200px;color:#d3dae7;font-size:11px;line-height:1.4}
.area-rule{left:162px;top:2378px;width:84px;height:7px;background:var(--white)}
.svc{width:205px;display:flex;gap:10px}
.svc svg{flex:none}
.svc h4{font-size:12px;font-weight:500;color:var(--navy)}
.svc p{font-size:7.5px;color:var(--muted);line-height:1.35;margin-top:4px}

/* request */
.req-title{left:160px;top:2458px}
.req-intro{left:160px;top:2520px;width:560px}
.field{left:398px;width:402px}
.field label{display:block;font-size:18px;font-weight:400;color:var(--ink)}
.field .ph{font-size:11px;color:#8a8a8a;padding:2px 0 4px;border-bottom:3px solid var(--line)}
.field .tall{height:64px}
.submit{left:475px;top:2952px;width:237px;height:46px;border:3px solid var(--accent);font-size:20px;font-weight:600;display:flex;align-items:center;justify-content:center}

/* footer */
.footer{left:0;top:3065px;width:1200px;height:220px;background:var(--navy-deep)}
.foot-brand{left:162px;top:3110px;display:flex;align-items:center;gap:10px}
.foot-brand .brand-name{color:var(--white)}
.foot-links{left:370px;top:3110px;color:var(--white);font-size:13px;line-height:1.9;text-transform:uppercase}
.foot-contact{left:642px;top:3108px;color:var(--white);font-size:14px;font-weight:300}
.foot-contact div{display:flex;gap:10px;align-items:flex-start;margin-bottom:14px}
.foot-map{left:832px;top:3105px;width:208px;height:154px;background:linear-gradient(135deg,#e7e4d8,#cfd8c4)}
</style>
</head>
<body>

<div class="abs hero" role="img" aria-label="Photo of a handyman wearing a tool belt with tools"></div>
<div class="abs hero-shade"></div>
<header class="abs topbar"></header>
<div class="abs brand"><span class="brand-mark"></span><span class="brand-name">Quillon Handyman Services</span></div>
<nav class="abs nav">
  <span class="active">Residentian Services by Room</span><span>About Us</span><span>Tips</span><span>Service Area</span><span>Service Request</span>
</nav>
<h1 class="abs hero-title">HONEST &amp; PROFESSIONAL</h1>
<div class="abs hero-sub">HOME REPAIR SERVICE PROVIDER</div>
<div class="abs hero-cta">Click here for your repairs</div>

<h2 class="abs h2 about-title">About Us</h2>
<p class="abs lead about-lead">Proin faucibus vitae mauris vel feugiat. Nulla gravida sollicitudin diam, mollis finibus purus condimentum sit amet.</p>
<p class="abs about-p1">Lorem ipsum dolor sit amet, consectetur adipiscing elit. Vestibulum at imperdiet odio, quis viverra eros. Sed a arcu nec mi placerat consequat nec at tellus. Quisque sit amet viverra augue.</p>
<p class="abs body-sm about-p2">Vivamus scelerisque mi in vehicula maximus. Donec dapibus enim sed nibh ultrices, ut iaculis nisi venenatis. Vestibulum enim nibh, interdum sed sagittis a, bibendum non neque. Morbi et condimentum justo. Mauris facilisis lectus sed gravida feugiat. Donec dapibus enim sed nibh ultrices, ut iaculis nisi venenatis. Vestibulum enim nibh, interdum sed sagittis a, bibendum non neque. Morbi et condimentum justo. Mauris facilisis lectus sed gravida feugiat.</p>

<section class="abs why"></section>
<h2 class="abs why-title">WHY CHOOSE US?</h2>
<p class="abs why-intro">Lorem ipsum dolor sit amet, consectetur adipiscing elit. Duis malesuada, felis eu efficitur bibendum, sem arcu.</p>
<div class="abs why-rule"></div>

<div class="abs feature" style="left:117px">
  <svg width="76" height="76" viewBox="0 0 76 76"><circle cx="38" cy="38" r="38" fill="var(--red)"/><path d="M24 52 L52 24 M24 24 L52 52" stroke="#fff" stroke-width="5" stroke-linecap="round"/><circle cx="24" cy="24" r="6" fill="none" stroke="#fff" stroke-width="3"/></svg>
  <h3>Professional Service</h3>
  <p>Vivamus scelerisque mi in vehicula maximus. Donec dapibus enim sed nibh ultrices, ut iaculis nisi venenatis. Vestibulum enim nibh, interdum sed sagittis a, bibendum non neque. Morbi et condimentum justo. Mauris facilisis lectus sed gravida feugiat.</p>
</div>
<div class="abs feature" style="left:362px">
  <svg width="76" height="76" viewBox="0 0 76 76"><circle cx="38" cy="38" r="38" fill="var(--orange)"/><circle cx="38" cy="38" r="24" fill="none" stroke="#fff" stroke-width="3"/><path d="M26 40 L38 29 L50 40 M30 38 V50 H46 V38" fill="none" stroke="#fff" stroke-width="3"/></svg>
  <h3>Honest</h3>
  <p>Vivamus scelerisque mi in vehicula maximus. Donec dapibus enim sed nibh ultrices, ut iaculis nisi venenatis. Vestibulum enim nibh, interdum sed sagittis a, bibendum non neque. Morbi et condimentum justo. Mauris facilisis lectus.</p>
</div>
<div class="abs feature" style="left:620px">
  <svg width="76" height="76" viewBox="0 0 76 76"><circle cx="38" cy="38" r="38" fill="var(--green)"/><circle cx="38" cy="38" r="18" fill="none" stroke="#1c3a10" stroke-width="3"/><text x="38" y="46" text-anchor="middle" font-family="Oswald,sans-serif" font-size="22" font-weight="700" fill="#1c3a10">$</text></svg>
  <h3>Low Cost</h3>
  <p>Vivamus scelerisque mi in vehicula maximus. Donec dapibus enim sed nibh ultrices, ut iaculis nisi venenatis. Vestibulum enim nibh, interdum sed sagittis a, bibendum non neque. Morbi et condimentum justo. Mauris facilisis lectus.</p>
</div>
<div class="abs feature" style="left:855px">
  <svg width="76" height="76" viewBox="0 0 76 76"><circle cx="38" cy="38" r="38" fill="var(--sky)"/><path d="M25 39 L34 48 L52 29" fill="none" stroke="#fff" stroke-width="5" stroke-linecap="round" stroke-linejoin="round"/></svg>
  <h3>Happy client</h3>
  <p>Vivamus scelerisque mi in vehicula maximus. Donec dapibus enim sed nibh ultrices, ut iaculis nisi venenatis. Vestibulum enim nibh, interdum sed sagittis a, bibendum non neque. Morbi et condimentum justo. Mauris facilisis lectus sed gravida feugiat.</p>
</div>

<h2 class="abs h2 tips-title">Tips</h2>
<p class="abs body-sm tips-intro">Vivamus scelerisque mi in vehicula maximus. Donec dapibus enim sed nibh ultrices, ut iaculis nisi venenatis. Vestibulum enim nibh, interdum sed sagittis a, bibendum non neque. Morbi et condimentum justo. Mauris facilisis lectus sed gravida feugiat.</p>

<article class="abs tip" style="top:1352px">
  <div class="tip-photo" role="img" aria-label="Photo of hands fixing a pipe fitting"></div>
  <div class="tip-body"><h3>Lorem Ipsum Dolor Sit</h3><p>Vivamus scelerisque mi in vehicula maximus. Donec dapibus enim sed nibh ultrices, ut iaculis nisi venenatis. Vestibulum enim nibh, interdum sed sagittis a, bibendum non neque. Morbi et condimentum justo. Mauris facilisis lectus sed gravida feugiat. Lorem ipsum dolor sit amet, consectetur adipiscing elit. Vestibulum at imperdiet odio, quis viverra eros. Sed a arcu nec mi placerat consequat nec at tellus. Quisque sit amet viverra augue. <b>More...</b></p>
  <div class="shares"><span style="background:var(--green)"></span><span style="background:var(--sky)"></span><span style="background:var(--navy)"></span><span style="background:var(--red)"></span></div></div>
</article>
<article class="abs tip" style="top:1496px">
  <div class="tip-photo" role="img" aria-label="Photo of a worker repairing a window frame"></div>
  <div class="tip-body"><h3>Lorem Ipsum Dolor Sit</h3><p>Vivamus scelerisque mi in vehicula maximus. Donec dapibus enim sed nibh ultrices, ut iaculis nisi venenatis. Vestibulum enim nibh, interdum sed sagittis a, bibendum non neque. Morbi et condimentum justo. Mauris facilisis lectus sed gravida feugiat. Lorem ipsum dolor sit amet, consectetur adipiscing elit. Vestibulum at imperdiet odio, quis viverra eros. Sed a arcu nec mi placerat consequat nec at tellus. Quisque sit amet viverra augue. <b>More...</b></p>
  <div class="shares"><span style="background:var(--green)"></span><span style="background:var(--sky)"></span><span style="background:var(--navy)"></span><span style="background:var(--red)"></span></div></div>
</article>
<article class="abs tip" style="top:1640px">
  <div class="tip-photo" role="img" aria-label="Photo of a handyman fixing a cabinet hinge"></div>
  <div class="tip-body"><h3>Lorem Ipsum Dolor Sit</h3><p>Vivamus scelerisque mi in vehicula maximus. Donec dapibus enim sed nibh ultrices, ut iaculis nisi venenatis. Vestibulum enim nibh, interdum sed sagittis a, bibendum non neque. Morbi et condimentum justo. Mauris facilisis lectus sed gravida feugiat. Lorem ipsum dolor sit amet, consectetur adipiscing elit. Vestibulum at imperdiet odio, quis viverra eros. Sed a arcu nec mi placerat consequat nec at tellus. Quisque sit amet viverra augue. <b>More...</b></p>
  <div class="shares"><span style="background:var(--green)"></span><span style="background:var(--sky)"></span><span style="background:var(--navy)"></span><span style="background:var(--red)"></span></div></div>
</article>
<article class="abs tip" style="top:1784px">
  <div class="tip-photo" role="img" aria-label="Photo of a plumber tightening a faucet"></div>
  <div class="tip-body"><h3>Lorem Ipsum Dolor Sit</h3><p>Vivamus scelerisque mi in vehicula maximus. Donec dapibus enim sed nibh ultrices, ut iaculis nisi venenatis. Vestibulum enim nibh, interdum sed sagittis a, bibendum non neque. Morbi et condimentum justo. Mauris facilisis lectus sed gravida feugiat. Lorem ipsum dolor sit amet, consectetur adipiscing elit. Vestibulum at imperdiet odio, quis viverra eros. Sed a arcu nec mi placerat consequat nec at tellus. Quisque sit amet viverra augue. <b>More...</b></p>
  <div class="shares"><span style="background:var(--green)"></span><span style="background:var(--sky)"></span><span style="background:var(--navy)"></span><span style="background:var(--red)"></span></div></div>
</article>
<article class="abs tip" style="top:1928px">
  <div class="tip-photo" style="background:linear-gradient(135deg,#8ea4c4,#4f6a92)" role="img" aria-label="Photo of a window screen being repaired"></div>
  <div class="tip-body"><h3>Lorem Ipsum Dolor Sit</h3><p>Vivamus scelerisque mi in vehicula maximus. Donec dapibus enim sed nibh ultrices, ut iaculis nisi venenatis. Vestibulum enim nibh, interdum sed sagittis a, bibendum non neque. Morbi et condimentum justo. Mauris facilisis lectus sed gravida feugiat. Lorem ipsum dolor sit amet, consectetur adipiscing elit. Vestibulum at imperdiet odio, quis viverra eros. Sed a arcu nec mi placerat consequat nec at tellus. Quisque sit amet viverra augue. <b>More...</b></p>
  <div class="shares"><span style="background:var(--green)"></span><span style="background:var(--sky)"></span><span style="background:var(--navy)"></span><span style="background:var(--red)"></span></div></div>
</article>
<div class="abs old-posts"><svg width="12" height="12" viewBox="0 0 12 12"><path d="M11 6H2M6 2L2 6L6 10" fill="none" stroke="var(--green)" stroke-width="2"/></svg>Old Posts</div>

<section class="abs area-panel"></section>
<h2 class="abs area-title">SERVICE AREA</h2>
<p class="abs area-text">Lorem ipsum dolor sit amet, consectetur adipiscing elit. Duis malesuada, felis eu efficitur bibendum, sem arcu sit amet, consectetur adipiscing elit. Duis malesuada, felis eu efficitur bibendum, sem arcu. Sit amet, consectetur adipiscing elit. Duis malesuada, felis eu efficitur bibendum, sem arcu.</p>
<div class="abs area-rule"></div>

<div class="abs svc" style="left:395px;top:2190px"><svg width="22" height="22" viewBox="0 0 22 22"><path d="M2 11L11 3L20 11H17V19H5V11Z" fill="var(--orange)"/></svg><div><h4>Tenant-Ready Properties</h4><p>Vivamus scelerisque mi in vehicula maximus. Donec dapibus enim sed nibh ultrices, ut iaculis nisi venenatis. Sed a arcu nec mi placerat consequat nec at tellus. Quisque sit amet viverra. <b>More...</b></p></div></div>
<div class="abs svc" style="left:620px;top:2190px"><svg width="22" height="22" viewBox="0 0 22 22"><circle cx="11" cy="11" r="9" fill="none" stroke="var(--red)" stroke-width="4"/></svg><div><h4>Insurance Claims &amp; Recovery</h4><p>Vivamus scelerisque mi in vehicula maximus. Donec dapibus enim sed nibh ultrices, ut iaculis nisi venenatis. Sed a arcu nec mi placerat consequat nec at tellus. Quisque sit amet viverra. <b>More...</b></p></div></div>
<div class="abs svc" style="left:850px;top:2190px"><svg width="22" height="22" viewBox="0 0 22 22"><circle cx="8" cy="9" r="5" fill="none" stroke="var(--accent)" stroke-width="3"/><circle cx="16" cy="16" r="4" fill="none" stroke="var(--accent)" stroke-width="3"/></svg><div><h4>Transparent, Proven Systems</h4><p>Vivamus scelerisque mi in vehicula maximus. Donec dapibus enim sed nibh ultrices, ut iaculis nisi venenatis. Sed a arcu nec mi placerat consequat nec at tellus. Quisque sit amet viverra. <b>More...</b></p></div></div>
<div class="abs svc" style="left:395px;top:2290px"><svg width="22" height="22" viewBox="0 0 22 22"><circle cx="11" cy="11" r="9" fill="var(--sky)"/></svg><div><h4>Solutions for Investors</h4><p>Vivamus scelerisque mi in vehicula maximus. Donec dapibus enim sed nibh ultrices, ut iaculis nisi venenatis. Sed a arcu nec mi placerat consequat nec at tellus. Quisque sit amet viverra. <b>More...</b></p></div></div>
<div class="abs svc" style="left:620px;top:2290px"><svg width="22" height="22" viewBox="0 0 22 22"><circle cx="11" cy="8" r="6" fill="var(--orange)"/><rect x="9.5" y="12" width="3" height="9" fill="var(--orange)"/></svg><div><h4>Construction &amp; Maintenance</h4><p>Vivamus scelerisque mi in vehicula maximus. Donec dapibus enim sed nibh ultrices, ut iaculis nisi venenatis. Sed a arcu nec mi placerat consequat nec at tellus. Quisque sit amet viverra. <b>More...</b></p></div></div>
<div class="abs svc" style="left:850px;top:2290px"><svg width="22" height="22" viewBox="0 0 22 22"><text x="11" y="19" text-anchor="middle" font-family="Oswald,sans-serif" font-size="22" font-weight="700" fill="var(--green)">$</text></svg><div><h4>Single-Source Services</h4><p>Vivamus scelerisque mi in vehicula maximus. Donec dapibus enim sed nibh ultrices, ut iaculis nisi venenatis. Sed a arcu nec mi placerat consequat nec at tellus. Quisque sit amet viverra. <b>More...</b></p></div></div>

<h2 class="abs h2 req-title">Service Request</h2>
<p class="abs body-sm req-intro">Vivamus scelerisque mi in vehicula maximus. Donec dapibus enim sed nibh ultrices, ut iaculis nisi venenatis. Vestibulum enim nibh, interdum sed sagittis a, bibendum non neque. Morbi et condimentum justo. Mauris facilisis lectus sed gravida feugiat.</p>

<div class="abs field" style="top:2585px"><label>Name:</label><div class="ph">insert your name</div></div>
<div class="abs field" style="top:2660px"><label>Email:</label><div class="ph">insert your email address</div></div>
<div class="abs field" style="top:2735px"><label>Subject:</label><div class="ph">insert your subject</div></div>
<div class="abs field" style="top:2810px"><label>Message:</label><div class="ph tall">insert your message</div></div>
<div class="abs submit">Submit</div>

<footer class="abs footer"></footer>
<div class="abs foot-brand"><span class="brand-mark"></span><span class="brand-name">Quillon Handyman Services</span></div>
<div class="abs foot-links">Residentian Services by Room<br>About Us<br>Tips<br>Service Area<br>Service Request</div>
<div class="abs foot-contact">
  <div><svg width="14" height="14" viewBox="0 0 14 14"><path d="M1 7L7 1L13 7H11V13H3V7Z" fill="#fff"/></svg><span>4th Street - Lorem Ipsum<br>Dolor Sit - 111111</span></div>
  <div><svg width="14" height="14" viewBox="0 0 14 14"><path d="M3 1L6 4L4.5 6Q6 9 8 9.5L10 8L13 11L11 13Q4 12 1 3Z" fill="#fff"/></svg><span>+123.456.789</span></div>
  <div><svg width="16" height="12" viewBox="0 0 16 12"><rect x="1" y="1" width="14" height="10" fill="none" stroke="#fff" stroke-width="1.5"/><path d="M1 1L8 7L15 1" fill="none" stroke="#fff" stroke-width="1.5"/></svg><span>youremail@domain.com</span></div>
</div>
<div class="abs foot-map" role="img" aria-label="Street map showing the office location"></div>

</body>
</html>
```